TELVIRA Web Page

We need a corporate web site for a new company TELVIRA Corporation. TELVIRA is a technology company that has developed a new virtualization solution for corporate applications. Our target customers are IT professionals. We have a logo, which we will provide.

Final design should communicate: innovation, stability, professionalism

Industry/Entity Type

It Company

```html
<!DOCTYPE html>
<html lang="en">
<head>
<meta charset="utf-8">
<title>TELVIRA – Virtualization Solution for IT Professionals</title>
<link rel="stylesheet" href="https://fonts.googleapis.com/css2?family=Arimo:wght@400;700&family=Jost:wght@300;600;700&family=Oswald:wght@300;500&display=swap">
<style>
:root{
  --blue:#0b85bf;
  --blue-dark:#0a6fa2;
  --green:#a3c21e;
  --green-text:#8cb00e;
  --ink:#1a1a1a;
  --grey:#555;
  --white:#fff;
}
*{margin:0;padding:0;box-sizing:border-box}
html,body{width:784px;height:1200px;overflow:hidden;background:var(--white)}
body{position:relative;font-family:Arimo,Arial,sans-serif;color:var(--ink)}
.abs{position:absolute}
.site-header{left:0;top:0;width:784px;height:83px;background:var(--blue);border-bottom:3px solid var(--blue-dark)}
.logo{left:12px;top:7px;width:132px;height:68px;border-radius:50%;background:var(--white);display:flex;align-items:center;justify-content:center;font-family:Arimo,sans-serif;font-weight:700;font-size:20px;color:var(--blue-dark);letter-spacing:1px}
.tagline{left:230px;top:28px;width:320px;text-align:center;font-family:Oswald,sans-serif;font-weight:300;font-size:21px;color:var(--white);letter-spacing:-.3px}
.tagline strong{font-weight:500}
.tollfree{right:17px;top:15px;text-align:right;color:var(--white)}
.tollfree .label{font-size:14px}
.tollfree .number{display:flex;align-items:center;gap:6px;font-family:Oswald,sans-serif;font-weight:300;font-size:27px;margin-top:1px}
.main-nav{left:0;top:86px;width:784px;height:33px;background:var(--green);display:flex;padding-left:10px}
.main-nav a{color:var(--white);text-decoration:none;font-size:12.5px;line-height:33px;font-family:Arimo,sans-serif}
.main-nav a.active{background:var(--blue);width:85px;text-align:center;margin-right:35px}
.main-nav a.n{margin-right:0}
.hero{left:0;top:119px;width:784px;height:305px;background:radial-gradient(circle at 45% 50%,#e6c4a6 0 12%,transparent 30%),radial-gradient(circle at 35% 40%,#9edcf0 0,transparent 40%),linear-gradient(90deg,#3f8fb0,#8fcde6 45%,#bfe6f3 75%,#7fc6e0)}
h2.section-title{font-family:Jost,sans-serif;font-weight:300;font-size:31px;color:var(--blue)}
.why{left:24px;top:447px;width:400px}
.why p{font-size:9.6px;line-height:11.6px;margin-top:15px;color:#222}
.checklist{list-style:none;margin-top:17px}
.checklist li{display:flex;align-items:center;gap:10px;font-size:9.6px;height:20.2px;padding-left:10px}
.news{left:528px;top:449px;width:211px}
.news-item{display:flex;gap:17px;padding:12px 0 14px;border-bottom:1px dotted #999}
.date{width:26px;text-align:center;color:var(--blue);font-size:10px;font-weight:700}
.date .day{width:26px;height:26px;border-radius:50%;background:var(--blue);border:2px solid #bfe1f1;color:var(--white);font-family:Oswald,sans-serif;font-weight:500;font-size:14px;line-height:22px;margin:1px 0 6px}
.news-item h3{font-size:9.6px;font-weight:700}
.news-item p{font-size:8.3px;line-height:10.5px;color:var(--grey);margin-top:6px}
.more{font-size:8.3px;font-weight:700;color:var(--green-text);margin-top:2px}
.more-news{text-align:right;font-size:9px;color:var(--green-text);margin-top:11px}
.feature{top:750px;width:215px}
.feature .icon{margin-left:44px;width:86px;height:68px;position:relative}
.feature h3{font-family:Jost,sans-serif;font-weight:600;font-size:16px;color:var(--blue);margin-top:16px}
.feature p{font-size:9.2px;line-height:11.6px;color:var(--grey);margin-top:8px}
.feature .readmore{font-size:9px;font-weight:700;color:#555;margin-top:7px}
.partners{left:0;top:980px;width:784px;height:86px;background:linear-gradient(#f3f3f3,#fff 15%,#fff 85%,#f3f3f3)}
.partner-row{left:40px;top:0;width:704px;height:86px;display:flex;align-items:center;justify-content:space-around}
.partner{display:flex;align-items:center;gap:5px;font-family:Arimo,sans-serif;font-weight:700;font-size:15px;color:#1e2a4a}
.arrow{top:22px;font-family:Jost,sans-serif;font-weight:300;font-size:34px;color:#777}
.site-footer{left:0;top:1105px;width:784px;height:95px;background:var(--blue)}
.social{left:0;top:15px;width:784px;display:flex;justify-content:center;gap:8px}
.social span{width:20px;height:20px;border-radius:50%;background:var(--white)}
.footer-rule{left:170px;top:48px;width:444px;height:1px;background:#2a97cb}
.footer-nav{left:0;top:58px;width:784px;text-align:center;font-size:9.6px}
.footer-nav a{color:#e8f040;text-decoration:none;margin:0 1px}
.copyright{left:0;top:75px;width:784px;text-align:center;font-size:8.3px;color:#7fc2e4}
</style>
</head>
<body>
<header class="abs site-header">
  <div class="abs logo">TELVIRA</div>
  <div class="abs tagline">Virtualization Solution for <strong>IT Professionals</strong></div>
  <div class="abs tollfree">
    <div class="label">Toll free call now!</div>
    <div class="number">
      <svg width="26" height="26" viewBox="0 0 26 26"><circle cx="13" cy="13" r="11.5" fill="none" stroke="#fff" stroke-width="2"/><path d="M9 7c-1 1-1.5 2.5-.5 5s3 5 5.5 6 3.5.5 4.5-.5l-2.5-2.5-1.5 1c-1.5-.5-3-2-3.5-3.5l1-1.5z" fill="#fff"/></svg>
      0400 812 377
    </div>
  </div>
</header>
<nav class="abs main-nav">
  <a class="active" href="#">Home</a>
  <a href="#" style="margin-left:20px">Services</a>
  <a href="#" style="margin-left:90px">Solutions</a>
  <a href="#" style="margin-left:90px">Partners</a>
  <a href="#" style="margin-left:85px">About Us</a>
  <a href="#" style="margin-left:90px">Contact</a>
</nav>
<div class="abs hero" role="img" aria-label="Photo of a hand touching a glowing digital interface of circles and binary code"></div>

<section class="abs why">
  <h2 class="section-title">Why TELVIRA</h2>
  <p>Lorem ipsum dolor sit amet, consectetur adipisicing elit, sed do eiusmod tempor incididunt ut l abore et dolore magna aliqua. Ut enim ad minim veniam, quis nostrud exercitation ullamco laboris nisi ut aliquip ex ea commodo consequat. Duis aute irure dolor in reprehenderit in voluptate velit esse cillum dolore eu fugiat nulla pariatur. Excepteur sint occaecat cupidatat non proident, sunt in culpa qui officia deserunt mollit anim id est laborum.</p>
  <ul class="checklist">
    <li><svg width="13" height="13" viewBox="0 0 13 13"><circle cx="6.5" cy="6.5" r="6" fill="#2a2a2a"/><path d="M3 6.5l2.5 2.5L11 2" fill="none" stroke="#7cc21e" stroke-width="2.2"/></svg>Sed ut perspiciatis, unde omnis iste natus error sit voluptatem accusantium</li>
    <li><svg width="13" height="13" viewBox="0 0 13 13"><circle cx="6.5" cy="6.5" r="6" fill="#2a2a2a"/><path d="M3 6.5l2.5 2.5L11 2" fill="none" stroke="#7cc21e" stroke-width="2.2"/></svg>Doloremque laudantium, totam rem aperiam eaque ipsa, quae ab illo inventore</li>
    <li><svg width="13" height="13" viewBox="0 0 13 13"><circle cx="6.5" cy="6.5" r="6" fill="#2a2a2a"/><path d="M3 6.5l2.5 2.5L11 2" fill="none" stroke="#7cc21e" stroke-width="2.2"/></svg>Veritatis et quasi architecto beatae vitae dicta sunt, explicabo.</li>
    <li><svg width="13" height="13" viewBox="0 0 13 13"><circle cx="6.5" cy="6.5" r="6" fill="#2a2a2a"/><path d="M3 6.5l2.5 2.5L11 2" fill="none" stroke="#7cc21e" stroke-width="2.2"/></svg>Nemo enim ipsam voluptatem, quia voluptas sit, aspernatur aut odit aut fugit</li>
    <li><svg width="13" height="13" viewBox="0 0 13 13"><circle cx="6.5" cy="6.5" r="6" fill="#2a2a2a"/><path d="M3 6.5l2.5 2.5L11 2" fill="none" stroke="#7cc21e" stroke-width="2.2"/></svg>Quia consequuntur magni dolores eos, qui ratione voluptatem sequi nesciunt</li>
  </ul>
</section>

<aside class="abs news">
  <h2 class="section-title">Latest News</h2>
  <div class="news-item" style="margin-top:10px">
    <div class="date"><div class="day">07</div>AUG</div>
    <div><h3>Lorem ipsum dolor sit amet</h3><p>Lorem ipsum dolor sit amet, consectetur adipisicing elit, sed do.</p><div class="more">read more +</div></div>
  </div>
  <div class="news-item">
    <div class="date"><div class="day">07</div>AUG</div>
    <div><h3>Lorem ipsum dolor sit amet</h3><p>Lorem ipsum dolor sit amet, consectetur adipisicing elit, sed do.</p><div class="more">read more +</div></div>
  </div>
  <div class="more-news">more news +</div>
</aside>

<section class="abs feature" style="left:31px">
  <svg class="icon" viewBox="0 0 86 68"><circle cx="52" cy="34" r="34" fill="#a3c21e"/><circle cx="34" cy="34" r="34" fill="#0b85bf"/><path d="M20 38a8 8 0 0 1 3-15 11 11 0 0 1 21 2 7 7 0 0 1 2 13z" fill="#fff"/><path d="M26 44q8 5 16 0M29 49q5 3 10 0" fill="none" stroke="#fff" stroke-width="2.2"/></svg>
  <h3>At Vero Eos Et</h3>
  <p>Xos et accusamus et iusto odio dignissimos ducimus, qui blanditiis praesentium voluptatum deleniti atque corrupti, quos dolores et quas molestias excepturi</p>
  <div class="readmore">read more +</div>
</section>
<section class="abs feature" style="left:287px">
  <svg class="icon" viewBox="0 0 86 68"><circle cx="52" cy="34" r="34" fill="#a3c21e"/><circle cx="34" cy="34" r="34" fill="#0b85bf"/><rect x="22" y="22" width="24" height="17" rx="2" fill="#fff"/><rect x="17" y="41" width="34" height="4" rx="1.5" fill="#fff"/></svg>
  <h3>IT Accusamus Et Iusto</h3>
  <p>Et harum quidem rerum facilis est et expedita distinctio. Nam libero tempore, cum soluta nobis est eligendi optio, cumque nihil impedit, quo minus id, quod maxime placeat, facere</p>
  <div class="readmore">read more +</div>
</section>
<section class="abs feature" style="left:543px">
  <svg class="icon" viewBox="0 0 86 68"><circle cx="52" cy="34" r="34" fill="#a3c21e"/><circle cx="34" cy="34" r="34" fill="#0b85bf"/><circle cx="34" cy="26" r="7" fill="#fff"/><path d="M19 48q2-13 15-13t15 13z" fill="#fff"/></svg>
  <h3>Dignissimos Ducimus</h3>
  <p>qui dolorem ipsum, quia dolor sit amet, conse adipisci[ng] velit, sed quia non numquam [do] modi tempora inci[di]dunt, ut labore et dolore magnam aliquam quaerat voluptatem.</p>
  <div class="readmore">read more +</div>
</section>

<section class="abs partners">
  <div class="abs arrow" style="left:6px">‹</div>
  <div class="abs partner-row">
    <span class="partner"><svg width="14" height="14"><circle cx="7" cy="7" r="7" fill="#1593c9"/></svg>Norvale</span>
    <span class="partner">Kestrel Data</span>
    <span class="partner" style="color:#666">Hypervane</span>
    <span class="partner"><svg width="26" height="46"><rect x="1" y="1" width="24" height="44" fill="none" stroke="#1e2a4a" stroke-width="2"/></svg>Paylink</span>
    <span class="partner">Voltara</span>
    <span class="partner"><svg width="40" height="40"><circle cx="20" cy="20" r="20" fill="#1592b5"/></svg>Orbex Lab</span>
    <span class="partner" style="color:#2b4fa8">Quarrix</span>
  </div>
  <div class="abs arrow" style="right:6px">›</div>
</section>

<footer class="abs site-footer">
  <div class="abs social"><span></span><span></span><span></span><span></span><span></span></div>
  <div class="abs footer-rule"></div>
  <nav class="abs footer-nav"><a href="#">Home</a> <a href="#">Services</a> <a href="#">Solutions</a> <a href="#">Partners</a> <a href="#">About Us</a> <a href="#">Contact</a></nav>
  <div class="abs copyright">© Copyright 2013 TELVIRA. All Rights Reserved</div>
</footer>
</body>
</html>
```